Business Card/ Car Magnet/ Polo Shirt/ Envelope/ Letterhead Design Project
Birchmont Property Valuations, LLC.
Business Card/ Car Magnet/ Polo Shirt/ Envelope/ Letterhead Design Project - Real Estate
Creative Brief
Professional
Gus Talbottine
State Certified Residential Real Estate Appraiser
14 Coldmeadow Ln Sewell, NJ 08080
gtalbottine@birchmontvaluations.example
valuemarkhq.example
NJ- 57RC00913400 PA- RL284615 DE- X2-0000317
Please be creative...
gust1983 gust1983
Hello, Just wanted to clarify some of the common questions asked so far. The colors to incorporate would be blue, green and white (unless of course you would like to incorporate other colors for creativity) . please feel free to incorporate them any way you see fit. The polo shirts will be done on white, black and royal blue shirts. Please be as creative as you like. Thanks you for your efforts and for participating! Please reply back with any further questions. Thanks! BPV

```html
<!DOCTYPE html>
<html lang="en">
<head>
<meta charset="utf-8">
<title>Birchmont Property Valuations – Business Card</title>
<link rel="stylesheet" href="https://fonts.googleapis.com/css2?family=Open+Sans:wght@400;600&display=swap">
<style>
  :root {
    --bg: #e6e8eb;
    --card: #ffffff;
    --blue-dark: #1a4f9c;
    --blue-mid: #2a78c8;
    --blue-light: #5fb2ea;
    --green: #6cb33f;
    --ink: #222a33;
    --brand: #1e3f7a;
    --rule: #9aa4ae;
  }
  * { box-sizing: border-box; margin: 0; padding: 0; }
  html, body { width: 1200px; height: 782px; overflow: hidden; }
  body {
    background: var(--bg);
    font-family: "Open Sans", Arial, sans-serif;
    display: flex;
    align-items: center;
    justify-content: center;
    gap: 48px;
  }
  .card {
    position: relative;
    width: 540px;
    height: 310px;
    background: var(--card);
    border-radius: 24px;
    overflow: hidden;
    box-shadow: 0 6px 18px rgba(0,0,0,.15);
  }
  .card__swoosh { position: absolute; inset: 0; width: 100%; height: 100%; }
  .brand {
    position: absolute;
    display: flex;
    flex-direction: column;
    align-items: center;
    color: var(--brand);
    font-weight: 600;
  }
  .brand__dot {
    width: 38px; height: 38px;
    border-radius: 50%;
    background: var(--green);
    margin-bottom: 8px;
  }
  .brand__mark { font-size: 40px; line-height: 1; letter-spacing: 2px; }
  .brand__name {
    font-size: 9px;
    letter-spacing: .6px;
    text-transform: uppercase;
    margin-top: 6px;
    padding-top: 4px;
    border-top: 1px solid var(--brand);
  }
  .card--back .brand { left: 0; right: 0; top: 108px; }
  .card--front .brand { left: 40px; top: 130px; }
  .holder {
    position: absolute;
    right: 26px;
    top: 20px;
    text-align: right;
    color: #fff;
  }
  .holder__name { font-size: 15px; font-weight: 600; }
  .holder__role { font-size: 12px; }
  .contact {
    position: absolute;
    left: 292px;
    top: 148px;
    padding-left: 14px;
    border-left: 1px solid var(--rule);
    color: var(--ink);
    font-size: 12.5px;
    line-height: 18px;
  }
  .contact__row { display: flex; align-items: center; gap: 6px; }
  .contact__icon { width: 11px; height: 11px; fill: var(--blue-dark); flex: none; }
</style>
</head>
<body>

<svg width="0" height="0" style="position:absolute">
  <defs>
    <linearGradient id="band-blue" x1="0" y1="0" x2="1" y2="0">
      <stop offset="0" stop-color="#5fb2ea"/>
      <stop offset="0.5" stop-color="#2a78c8"/>
      <stop offset="1" stop-color="#1a4f9c"/>
    </linearGradient>
  </defs>
</svg>

<section class="card card--back" aria-label="Card back">
  <svg class="card__swoosh" viewBox="0 0 540 310" aria-hidden="true">
    <path d="M0 0 H540 V78 C420 40 230 22 0 30 Z" fill="url(#band-blue)"/>
    <path d="M0 40 C230 30 420 48 540 92 V98 C420 56 230 38 0 44 Z" fill="var(--green)"/>
  </svg>
  <div class="brand">
    <span class="brand__dot"></span>
    <span class="brand__mark">BPV</span>
    <span class="brand__name">Birchmont Property Valuations, LLC.</span>
  </div>
</section>

<section class="card card--front" aria-label="Card front">
  <svg class="card__swoosh" viewBox="0 0 540 310" aria-hidden="true">
    <path d="M0 0 H540 V88 C420 44 230 24 0 30 Z" fill="url(#band-blue)"/>
    <path d="M0 40 C230 32 420 52 540 102 V108 C420 60 230 40 0 44 Z" fill="var(--green)"/>
  </svg>
  <div class="holder">
    <div class="holder__name">Marlo Quenby-Hart</div>
    <div class="holder__role">Consultant</div>
  </div>
  <div class="brand">
    <span class="brand__dot"></span>
    <span class="brand__mark">BPV</span>
    <span class="brand__name">Birchmont Property Valuations, LLC.</span>
  </div>
  <div class="contact">
    <div>27 Ashgrove Ave, 4th floor</div>
    <div>Linden Park, Eastvale</div>
    <div class="contact__row">
      <svg class="contact__icon" viewBox="0 0 12 12"><path d="M2.5 0.5 L4.5 0.5 L5.3 3.2 L4 4.3 C4.7 5.8 6 7.2 7.6 8 L8.7 6.7 L11.5 7.5 V9.5 C11.5 10.6 10.6 11.5 9.5 11.5 C4.5 11.2 0.8 7.5 0.5 2.5 C0.5 1.4 1.4 0.5 2.5 0.5 Z"/></svg>
      <span>012 555 0142</span>
    </div>
    <div class="contact__row">
      <svg class="contact__icon" viewBox="0 0 12 12"><path d="M3 0 H9 A1 1 0 0 1 10 1 V11 A1 1 0 0 1 9 12 H3 A1 1 0 0 1 2 11 V1 A1 1 0 0 1 3 0 Z M3.2 1.5 V9 H8.8 V1.5 Z"/></svg>
      <span>012 555 0142</span>
    </div>
    <div class="contact__row">
      <svg class="contact__icon" viewBox="0 0 12 12"><path d="M0 2 H12 V10 H0 Z M0.8 2.6 L6 6.6 L11.2 2.6 L11.2 3.6 L6 7.6 L0.8 3.6 Z" fill-rule="evenodd"/></svg>
      <span>yourname@mail.example</span>
    </div>
    <div>www.yoursite.example</div>
  </div>
</section>

</body>
</html>
```